Awesome Web Design Project

must have a link to mingleton of the homepage preferably a scrolling view of our mingleton page!

We are an exciting new electrical company with a strong focus on energy efficiency and offering the latest technologies.

The design should allow easy navigation, there shouldn't be too many menus, It should look clean and sleek, Colours to consider could be green, silver/chrome, black,

The site should convey technology, efficiency and simplicity

Must be viewable on all devices, pc's, tablets, phones ie Responsive
Updates

Logo and some pics uploaded!

Industry/Entity Type

Electrical

Requirements
Must have
• must include the following pages,
about us
our services
gallery
contact us
Connect with us
Nice to have
• Would be great if the website design used a user friendly cms,
Should not have
• too many links, menus, clutter it should be clean and easy to navigate

```html
<!DOCTYPE html>
<html lang="en">
<head>
<meta charset="utf-8">
<title>Kestrel Electrical — Home</title>
<link rel="stylesheet" href="https://fonts.googleapis.com/css2?family=Oswald:wght@300;400;500&family=Noto+Sans:wght@400;700&display=swap">
<style>
  :root {
    --ink: #1e1e1e;
    --nav-ink: #444444;
    --accent: #d5de1e;
    --accent-ink: #1d3557;
    --social: #3b5998;
    --white: #ffffff;
    --band: #ececec;
    --rule: #d8d8d8;
    --arrow-bg: rgba(190, 190, 190, 0.75);
    --hero-dark: #2a2a2a;
    --hero-mid: #5a5a5a;
  }
  * { box-sizing: border-box; margin: 0; padding: 0; }
  html, body { width: 1200px; height: 900px; overflow: hidden; }
  body { position: relative; background: #050505; font-family: "Noto Sans", Arial, sans-serif; color: var(--ink); }

  .hero {
    position: absolute; left: 0; top: 92px; width: 1200px; height: 560px;
    background: radial-gradient(ellipse at 55% 20%, #8a8a8a 0%, var(--hero-mid) 35%, var(--hero-dark) 80%);
  }
  .topbar { position: absolute; left: 0; top: 0; width: 1200px; height: 32px; background: #050505; }

  .site-nav {
    position: absolute; left: 16px; top: 32px; width: 1170px; height: 60px;
    background: var(--white);
  }
  .brand { position: absolute; left: 22px; top: 13px; display: flex; align-items: center; gap: 10px; }
  .brand-square { width: 34px; height: 34px; background: var(--accent); }
  .brand-name {
    font-family: "Oswald", sans-serif; font-weight: 400; color: var(--nav-ink);
    font-size: 22px; letter-spacing: 3px; line-height: 1;
  }
  .nav-links { list-style: none; }
  .nav-links li {
    position: absolute; top: 0; height: 60px; display: flex; align-items: center;
    font-family: "Oswald", sans-serif; font-weight: 400; font-size: 17.5px; color: var(--nav-ink);
    white-space: nowrap;
  }
  .nav-about { left: 483px; }
  .nav-services { left: 591px; }
  .nav-gallery { left: 735px; }
  .nav-contact { left: 843px; }
  .nav-links .caret { display: inline-block; margin-left: 6px; border: 4px solid transparent; border-top: 5px solid var(--nav-ink); transform: translateY(2px); }
  .nav-connect {
    position: absolute; left: 937px; top: 0;
    background: var(--accent); color: var(--accent-ink); font-weight: 700; font-size: 16px;
    width: 171px; height: 60px; display: flex; align-items: center; justify-content: center;
  }
  .nav-social {
    position: absolute; left: 1108px; top: 0;
    background: var(--social); color: var(--white); width: 62px; height: 60px;
    display: flex; align-items: center; justify-content: center; font-size: 11px; font-weight: 700;
  }

  .hero-copy { position: absolute; left: 250px; top: 285px; width: 700px; text-align: center; color: var(--white); z-index: 2; }
  .hero-title { font-family: "Oswald", sans-serif; font-weight: 400; font-size: 63px; line-height: 80px; }
  .hero-title em { font-style: normal; color: var(--accent); }
  .hero-lead { font-family: "Oswald", sans-serif; font-weight: 400; font-size: 18px; line-height: 25px; text-transform: uppercase; margin-top: 8px; }
  .hero-lead span { display: block; white-space: nowrap; }
  .hero-more {
    display: block; margin: 20px auto 0; width: 81px; height: 27px; background: var(--accent);
    color: var(--ink); font-family: "Oswald", sans-serif; font-size: 15px; line-height: 27px;
  }
  .slider-arrow {
    position: absolute; top: 343px; width: 55px; height: 58px; background: var(--arrow-bg);
    display: flex; align-items: center; justify-content: center; z-index: 2;
  }
  .slider-arrow.prev { left: 0; }
  .slider-arrow.next { right: 0; }

  .features { position: absolute; left: 0; top: 652px; width: 1200px; height: 248px; background: var(--band); }
  .feature-photo {
    position: absolute; width: 196px; height: 196px; border-radius: 50%;
    border: 3px solid var(--white); z-index: 3;
  }
  .photo-lounge { left: 102px; top: 537px; background: linear-gradient(160deg, #9b9b9b, #4a4a4a 60%, #cfcfcf); }
  .photo-library { left: 499px; top: 533px; background: linear-gradient(90deg, #6b5a4a 0%, #c9ccd2 35%, #e9ecef 70%, #b8bcc2 100%); }
  .photo-ceiling { left: 910px; top: 533px; background: linear-gradient(180deg, #d9dde2 0%, #f4f6f8 50%, #a9c4d1 100%); }

  .feature-heading { position: absolute; font-family: "Oswald", sans-serif; font-weight: 400; color: var(--ink); text-transform: uppercase; }
  .feature-text { position: absolute; width: 322px; font-size: 13.4px; line-height: 20px; text-align: justify; color: #333; }
  .who h2 { left: 47px; top: 752px; font-size: 21px; }
  .who p { left: 47px; top: 807px; }
  .offer h2 { left: 438px; top: 753px; font-size: 21px; }
  .offer-list { position: absolute; left: 432px; top: 790px; width: 328px; list-style: none; }
  .offer-list li { font-size: 16px; color: #444; padding: 5px 8px; line-height: 22px; border-bottom: 1px solid var(--rule); height: 36px; }
  .offer-list li + li { padding-top: 9px; height: 37px; }
  .tech h2 { left: 851px; top: 722px; line-height: 33px; }
  .tech h2 .big { font-size: 32px; display: block; }
  .tech h2 .small { font-size: 25px; display: block; }
  .tech p { left: 848px; top: 810px; }
</style>
</head>
<body>
  <div class="topbar"></div>
  <div class="hero" role="img" aria-label="Grayscale photo of a modern interior with angular LED strip lighting across the ceiling"></div>

  <header class="site-nav">
    <div class="brand">
      <span class="brand-square"></span>
      <span class="brand-name">KESTREL ELECTRICAL</span>
    </div>
    <ul class="nav-links">
      <li class="nav-about">ABOUT US</li>
      <li class="nav-services">OUR SERVICES<span class="caret"></span></li>
      <li class="nav-gallery">GALLERY</li>
      <li class="nav-contact">CONTACT US</li>
    </ul>
    <a class="nav-connect">CONNECT WITH US</a>
    <a class="nav-social">mingleton</a>
  </header>

  <div class="slider-arrow prev">
    <svg width="18" height="28" viewBox="0 0 18 28"><path d="M14 3 L4 14 L14 25" fill="none" stroke="#333" stroke-width="4"/></svg>
  </div>
  <div class="slider-arrow next">
    <svg width="18" height="28" viewBox="0 0 18 28"><path d="M4 3 L14 14 L4 25" fill="none" stroke="#333" stroke-width="4"/></svg>
  </div>

  <section class="hero-copy">
    <h1 class="hero-title">INNOVATION <em>EXPERT</em></h1>
    <p class="hero-lead"><span>Lorem Ipsum is simply dummy text of the printing and typesetting indus-</span><span>try. Lorem Ipsum has been the industry's standard dummy text ever</span><span>since the 1500s,</span></p>
    <a class="hero-more">MORE</a>
  </section>

  <section class="features"></section>
  <div class="feature-photo photo-lounge" role="img" aria-label="Living room with wall-mounted TV and media console"></div>
  <div class="feature-photo photo-library" role="img" aria-label="Bookshelves beside a ceiling with linear recessed lights"></div>
  <div class="feature-photo photo-ceiling" role="img" aria-label="Ceiling with angular LED light installation"></div>

  <div class="who">
    <h2 class="feature-heading">Who we are</h2>
    <p class="feature-text">Lorem Ipsum is simply dummy text of the printing and typesetting industry. Lorem Ipsum has been the industry's standard dummy text ever since the 1500s, when an unknown printer took a galley of type and scrambled it to make a type specimen book. ook a</p>
  </div>
  <div class="offer">
    <h2 class="feature-heading">What we offer</h2>
    <ul class="offer-list">
      <li>Residential / Commercial / Industrial</li>
      <li>Office / Lot Lighting</li>
      <li>Pools / Hot tubs / Spas</li>
    </ul>
  </div>
  <div class="tech">
    <h2 class="feature-heading"><span class="big">New</span><span class="small">Technologies</span></h2>
    <p class="feature-text">Lorem Ipsum is simply dummy text of the printing and typesetting industry. Lorem Ipsum has been the industry's standard dummy text ever since the 1500s, when an unknown printer took a galley of type and scrambled it to make a type specimen book. ook a</p>
  </div>
</body>
</html>
```